Buch-Cover-Design - Lemurion 3.1 - Morgenlied für die Seele der Erdenkinder
Das Design von Glasfalke wurde sehr schnell und professionell erstellt. Ich habe mich außerordentlich gut betreut gefühlt, zumal die Designerin zum einen die Vorgabe excellent umgesetzt und dabei noch eigene Impulse eingebracht hat. Ich bin glücklich und dankbar, sowie hochzufrieden!
Zielgruppe
Ich habe ein Buch geschrieben. Zielgruppe sind Menschen mit dem Genre Spiritualität, Persönlichkeitsentwicklung, Esoterik, Coaching
Aufgabenstellung
Mein Buchtitel lautet: Lemurion 3.1 - Morgenlied für die Seele der Erdenkinder. Es sollte in irgendeiner Form ein spirituelles Cover sein. Gerne darf da auch die 'Lebensblume' als geometrisches Muster in einem Teil des Bildes integriert sein. Die Farben sollten eher hell, weiß, gelb und/oder rosa/lila sein. Keine dunklen Farben. Strahlen wie Sonnenlicht sind auch sehr gut.
Das Buch erscheint in DIN A5 und hat ca. 160 Seiten. Ich freue mich sehr über Ihre Vorschläge! Dankeschön.

```html
<!DOCTYPE html>
<html lang="de">
<head>
<meta charset="utf-8">
<title>Lemurion 3.1 – Morgenlied für die Seele der Erdenkinder</title>
<link rel="stylesheet" href="https://fonts.googleapis.com/css2?family=Allura&family=Open+Sans:wght@400&display=swap">
<style>
  :root {
    --page-bg: #f1eeec;
    --coral: #f2543f;
    --rose: #f7339a;
    --magenta: #e531d6;
    --violet: #b23cf0;
    --lilac: #9d6cf2;
    --sky: #3fc6e0;
    --mist: #ffffff;
    --ink-light: #ffffff;
  }
  * { margin: 0; padding: 0; box-sizing: border-box; }
  html, body {
    width: 1200px;
    height: 964px;
    overflow: hidden;
    background: var(--page-bg);
  }
  .stage {
    width: 1200px;
    height: 964px;
    display: flex;
    align-items: center;
    justify-content: center;
  }
  .book-cover {
    position: relative;
    width: 680px;
    height: 900px;
    overflow: hidden;
    box-shadow: 0 4px 18px rgba(0,0,0,0.12);
  }
  .cover-artwork {
    position: absolute;
    inset: 0;
    background:
      radial-gradient(ellipse 30% 22% at 0% 30%, rgba(255,255,255,0.95), rgba(255,255,255,0) 70%),
      radial-gradient(ellipse 22% 18% at 0% 62%, rgba(255,255,255,0.9), rgba(255,255,255,0) 70%),
      radial-gradient(ellipse 28% 12% at 85% 5%, rgba(255,255,255,0.85), rgba(255,255,255,0) 70%),
      radial-gradient(ellipse 55% 30% at 35% 4%, var(--coral), rgba(242,84,63,0) 75%),
      radial-gradient(ellipse 60% 35% at 90% 95%, var(--sky), rgba(63,198,224,0) 70%),
      radial-gradient(ellipse 50% 35% at 20% 85%, var(--lilac), rgba(157,108,242,0) 75%),
      linear-gradient(170deg, var(--rose) 0%, var(--magenta) 45%, var(--violet) 75%, var(--lilac) 100%);
  }
  .cover-text {
    position: absolute;
    inset: 0;
    color: var(--ink-light);
    text-align: center;
  }
  .book-title {
    position: absolute;
    top: 270px;
    left: 0;
    right: 0;
    font-family: "Allura", cursive;
    font-weight: 400;
    font-size: 104px;
    line-height: 1;
  }
  .book-subtitle {
    position: absolute;
    top: 385px;
    left: 0;
    right: 0;
    font-family: "Open Sans", sans-serif;
    font-size: 30px;
    line-height: 1.2;
  }
  .book-author {
    position: absolute;
    bottom: 72px;
    left: 0;
    right: 0;
    font-family: "Allura", cursive;
    font-size: 52px;
  }
</style>
</head>
<body>
  <main class="stage">
    <article class="book-cover">
      <div class="cover-artwork" role="img" aria-label="Aquarellfläche in Koralle, Pink, Magenta, Lila und Türkis mit feinem weißem Muster der Blume des Lebens"></div>
      <div class="cover-text">
        <h1 class="book-title">Lemurion 3.1</h1>
        <p class="book-subtitle">Morgenlied für die<br>Seele der Erdenkinder</p>
        <p class="book-author">Hannelore Winkt</p>
      </div>
    </article>
  </main>
</body>
</html>
```